SEO Company Needs a Professional, Bold Business Card Design

Kelvo SEO
2487 N Harlow Ave #315
Austin, TX 78705
512-555-0184
http://www.kelvoseo-demo.com
Kelvo SEO is an internet marketing company specializing in SEO for higher-end businesses. We are looking for a professional and bold (edgy) design that communicates our forward thinking SEO strategies. Our typical client is a small to medium US business that has never had SEO work done on their website but does has active marketing. We want our business card design to instill confidence in our services through a professional and bold look. We we would also like the design elements to be in line with the services we offer - ranking client websites in the search engine results, namely Zarnix.
Design Specifics:
Card design should have square edges.
Design should be delivered in fully layered and editable PSD file. Designing in AI is fine but I need a PSD file in case we have any changes in contact information or need additional cards for employees.
The design should compliment the attached logo.
Company Name:
Kelvo SEO
Address:
2487 N Harlow Ave #315
Austin, TX 78705
Personal Info:
Dorian Welk
Owner
theboss@kelvoseo-demo.com
Phone:
877-555-0139 (KELVO UP)
Website:
http://www.kelvoseo-demo.com
Slogan:
Could Your Website Be Generating More Business?
Target Market(s)
High-end business owners - doctors, lawyers, specialists, business owners doing 250k in profit.
Industry/Entity Type
Internet
Contact Information for Business Card
Company Name:
Kelvo SEO
Address:
123 Some Road Ste 123
Austin, TX 78705
Personal Info:
Dorian Welk
Owner
theboss@kelvoseo-demo.com
Phone:
877-555-0139 (KELVO UP)
Website:
www.kelvoseo-demo.com
Slogan:
Requirements
Must have
- Card design should have square edges.
- Background should be WHITE only.
- Design should be delivered in fully layered and editable PSD file. Designing in AI is fine but I need a PSD file in case we have any changes in contact information or need additional cards for employees.

```html
<!DOCTYPE html>
<html lang="en">
<head>
<meta charset="utf-8">
<title>Kelvo SEO Business Card</title>
<link href="https://fonts.googleapis.com/css2?family=Open+Sans:wght@400;600;700&family=Fira+Sans+Condensed:wght@400&display=swap" rel="stylesheet">
<style>
  :root {
    --stage-top: #2a2a2a;
    --stage-bottom: #050505;
    --card-white: #ffffff;
    --navy: #132f52;
    --name-blue: #2c4a6e;
    --text-dark: #333a44;
    --brand-blue: #1f6fb2;
  }
  * { margin: 0; padding: 0; box-sizing: border-box; }
  html, body { width: 1200px; height: 900px; overflow: hidden; }
  body {
    background: linear-gradient(180deg, var(--stage-top) 0%, #151515 55%, var(--stage-bottom) 100%);
    font-family: "Open Sans", sans-serif;
    position: relative;
  }
  .card {
    position: absolute;
    width: 447px;
    height: 259px;
    background: var(--card-white);
    border-radius: 12px;
    overflow: hidden;
    box-shadow: 0 2px 6px rgba(0,0,0,0.45);
  }
  .card--front { left: 125px; top: 304px; }
  .card--back { left: 629px; top: 305px; width: 445px; height: 258px; }
  .band { position: absolute; left: 0; top: 0; width: 100%; height: 100%; }
  .band polygon { fill: var(--navy); }

  .brand {
    position: absolute;
    display: flex;
    align-items: center;
    color: var(--brand-blue);
    font-weight: 700;
    white-space: nowrap;
  }
  .brand__dot { border-radius: 50%; background: var(--navy); flex: none; }
  .card--front .brand { left: 232px; top: 52px; font-size: 30px; gap: 8px; }
  .card--front .brand__dot { width: 26px; height: 26px; }
  .card--back .brand { left: 92px; top: 92px; font-size: 46px; gap: 12px; }
  .card--back .brand__dot { width: 40px; height: 40px; }

  .person { position: absolute; left: 36px; top: 80px; }
  .person__name { font-size: 19.5px; font-weight: 600; color: var(--name-blue); line-height: 1.1; }
  .person__role { font-size: 13px; color: var(--text-dark); margin-top: 2px; }

  .contacts { position: absolute; left: 223px; top: 121px; list-style: none; }
  .contacts li { display: flex; align-items: center; gap: 7px; font-size: 13px; color: var(--text-dark); height: 17px; }
  .contacts svg { width: 9px; height: 9px; fill: var(--navy); }

  .slogan {
    position: absolute;
    left: 0; right: 0; top: 224px;
    text-align: center;
    font-family: "Fira Sans Condensed", sans-serif;
    font-size: 11.5px;
    color: var(--card-white);
  }
</style>
</head>
<body>
  <section class="card card--front">
    <svg class="band" viewBox="0 0 447 259" aria-hidden="true">
      <polygon points="0,193 88,226 182,177 277,226 395,158 393,148 447,150 447,259 0,259"/>
    </svg>
    <div class="brand"><span class="brand__dot"></span>Kelvo SEO</div>
    <div class="person">
      <p class="person__name">Jonathan Smith</p>
      <p class="person__role">Managing Director</p>
    </div>
    <ul class="contacts">
      <li><svg viewBox="0 0 10 10"><path d="M1 3 Q5 0 9 3 L8 4.5 L6.5 3.5 L3.5 3.5 L2 4.5 Z M2 5 H8 V9 H2 Z"/></svg>123-456-7890</li>
      <li><svg viewBox="0 0 10 10"><path d="M0 2 H10 V8 H0 Z" /><path d="M0 2 L5 6 L10 2" stroke="#fff" stroke-width="1" fill="none"/></svg>info@youremail.com</li>
      <li><svg viewBox="0 0 10 10"><path d="M6 1 L9 4 L6.5 6.5 L5.5 5.5 L7.5 4 L6 2.5 L4.5 4.5 L3.5 3.5 Z M4 9 L1 6 L3.5 3.5 L4.5 4.5 L2.5 6 L4 7.5 L5.5 5.5 L6.5 6.5 Z"/></svg>www.yourweb.com</li>
    </ul>
  </section>

  <section class="card card--back">
    <svg class="band" viewBox="0 0 445 258" aria-hidden="true">
      <polygon points="0,190 89,222 181,174 276,222 396,157 391,145 445,147 445,258 0,258"/>
    </svg>
    <div class="brand"><span class="brand__dot"></span>Kelvo SEO</div>
    <p class="slogan">Could Your Website Be Generating More Business?</p>
  </section>
</body>
</html>
```